Business Card Design

An energy company designed around renewable energy and energy storage that focuses on providing its energy at points on the grid that reduce costs and add value to the system.

Industry/Entity Type

Business

Contact Information for Business Card

Martin Dellacroix
Executive Vice President
41 K ST NE
Washington, DC 20017
240-555-0187
mdellacroix@brightvaleenergy.example

```html
<!DOCTYPE html>
<html lang="en">
<head>
<meta charset="utf-8">
<title>Business Card – Martin Dellacroix</title>
<link rel="stylesheet" href="https://fonts.googleapis.com/css2?family=Lato:wght@400;700&display=swap">
<style>
  :root {
    --orange: #f7891f;
    --black: #0a0a0a;
    --white: #ffffff;
    --backdrop: #9a9a9a;
    --card-w: 580px;
    --card-h: 330px;
  }
  * { box-sizing: border-box; margin: 0; padding: 0; }
  html, body { width: 1200px; height: 900px; overflow: hidden; }
  body {
    background: var(--backdrop);
    font-family: "Lato", Arial, sans-serif;
    display: flex;
    flex-direction: column;
    align-items: center;
    justify-content: center;
    gap: 60px;
  }
  .card {
    position: relative;
    width: var(--card-w);
    height: var(--card-h);
    overflow: hidden;
    display: flex;
    flex-direction: column;
  }
  .band { width: 100%; }
  .band--orange { background: var(--orange); }
  .band--black { background: var(--black); }

  .brand {
    display: flex;
    align-items: center;
    justify-content: center;
    gap: 14px;
    height: 100%;
  }
  .brand__square {
    width: 30px;
    height: 30px;
    background: var(--white);
  }
  .brand__name {
    color: var(--white);
    font-weight: 700;
    font-size: 19px;
    line-height: 1.05;
    letter-spacing: 2px;
    text-transform: uppercase;
  }

  /* Front */
  .front .band--top { height: 122px; }
  .front .band--info { height: 136px; display: flex; align-items: center; }
  .front .band--foot { flex: 1; }
  .person {
    width: 42%;
    padding-right: 22px;
    text-align: right;
    color: var(--white);
  }
  .person__name { font-size: 23px; font-weight: 400; line-height: 1.1; white-space: nowrap; }
  .person__title { color: var(--orange); font-size: 14px; margin-bottom: 6px; white-space: nowrap; }
  .person__address { font-size: 14px; line-height: 1.35; white-space: nowrap; }
  .contacts {
    width: 58%;
    padding-left: 12px;
    list-style: none;
    color: var(--white);
    font-size: 14px;
    line-height: 1.55;
  }
  .contacts li { display: flex; align-items: center; gap: 10px; white-space: nowrap; }
  .icon { width: 14px; height: 14px; flex: none; }

  /* Back */
  .back .band--top { height: 82px; }
  .back .band--mid { height: 180px; }
  .back .band--foot { flex: 1; }
</style>
</head>
<body>

  <section class="card front" aria-label="Business card front">
    <div class="band band--orange band--top">
      <div class="brand">
        <span class="brand__square"></span>
        <span class="brand__name">Martin<br>Dellacroix</span>
      </div>
    </div>
    <div class="band band--black band--info">
      <div class="person">
        <p class="person__name">Martin Dellacroix</p>
        <p class="person__title">Executive Vice President</p>
        <p class="person__address">41 K ST NE<br>Washington, DC 20017</p>
      </div>
      <ul class="contacts">
        <li>
          <svg class="icon" viewBox="0 0 14 14" aria-hidden="true"><rect width="14" height="14" rx="2" fill="#f7891f"/><path d="M3.5 4.5h7v1.5h-7zM4.5 6.5h5l1 4h-7z" fill="#0a0a0a"/></svg>
          240-555-0187
        </li>
        <li>
          <svg class="icon" viewBox="0 0 14 14" aria-hidden="true"><rect width="14" height="14" rx="2" fill="#f7891f"/><rect x="3" y="4" width="8" height="6" fill="#0a0a0a"/><path d="M3 4l4 3 4-3" stroke="#f7891f" fill="none"/></svg>
          mdellacroix@brightvaleenergy.example
        </li>
        <li>
          <svg class="icon" viewBox="0 0 14 14" aria-hidden="true"><rect width="14" height="14" rx="2" fill="#f7891f"/><path d="M5 9l4-4M4 7.5l-1 1a1.4 1.4 0 0 0 2 2l1-1M10 6.5l1-1a1.4 1.4 0 0 0-2-2l-1 1" stroke="#0a0a0a" stroke-width="1.4" fill="none"/></svg>
          brightvaleenergy.example
        </li>
      </ul>
    </div>
    <div class="band band--orange band--foot"></div>
  </section>

  <section class="card back" aria-label="Business card back">
    <div class="band band--black band--top"></div>
    <div class="band band--orange band--mid">
      <div class="brand">
        <span class="brand__square"></span>
        <span class="brand__name">Martin<br>Dellacroix</span>
      </div>
    </div>
    <div class="band band--black band--foot"></div>
  </section>

</body>
</html>
```